Accounting firm needs a postcard design

We need a postcard design for our accounting office for a advertising campaign mailing we do yearly from a mail list we create. We are a full-service accounting office that has been in business for 35 years. I have attached our logo in different formats along with a document with a description of the services we provide. I have also attached my business card and the business card of our CPA. The business cards will have contact information for the postcard design. The contact email that will need to be on the postcard is contact@marlowtaxpartners.com.

```html
<!DOCTYPE html>
<html lang="en">
<head>
<meta charset="utf-8">
<title>Marlow Tax Partners – Postcard</title>
<link rel="stylesheet" href="https://fonts.googleapis.com/css2?family=Arimo:wght@400;700&family=Tinos:wght@700&display=swap">
<style>
  :root{
    --navy:#1b2a6b;
    --blue:#1667b3;
    --blue-light:#3d8fd6;
    --green-dark:#1c8a33;
    --green:#4eab3a;
    --green-light:#8cc63f;
    --ink:#222222;
    --white:#ffffff;
    --photo-a:#c9cdd2;
    --photo-b:#6d7480;
  }
  *{margin:0;padding:0;box-sizing:border-box}
  html,body{width:1200px;height:816px;overflow:hidden;background:var(--white)}
  .postcard{position:relative;width:1200px;height:816px;overflow:hidden;background:var(--white);font-family:"Arimo",Arial,sans-serif;color:var(--ink)}
  .hero-photo{position:absolute;left:0;top:0;width:1200px;height:392px;
    clip-path:polygon(565px 0,1200px 0,1200px 392px,660px 392px);
    background:linear-gradient(135deg,var(--photo-a) 0%,#9aa1aa 45%,var(--photo-b) 100%)}
  .backdrop{position:absolute;left:0;top:0}
  .brand{position:absolute;left:55px;top:40px;width:360px;text-align:center}
  .brand-mark{width:86px;height:86px;border-radius:50%;background:var(--navy);margin:0 auto 30px}
  .brand-name{font-family:"Tinos","Times New Roman",serif;font-weight:700;font-size:25px;letter-spacing:1.5px;color:var(--navy);white-space:nowrap}
  .brand-tagline{font-size:12.5px;color:var(--ink);margin-top:4px;white-space:nowrap}
  .cpa-name{position:absolute;left:55px;top:216px;font-family:"Tinos","Times New Roman",serif;font-weight:700;font-size:37px;line-height:41px;color:var(--navy)}
  .promise{position:absolute;left:55px;top:304px;font-size:26px;line-height:32px;color:var(--ink)}
  .section-tab{position:absolute;left:0;top:386px;width:278px;height:60px;background:var(--blue);
    clip-path:polygon(0 0,100% 0,92% 100%,0 100%)}
  .section-tab::after{content:"";position:absolute;left:0;bottom:0;width:100%;height:5px;background:var(--blue-light)}
  .section-title{position:absolute;left:55px;top:394px;font-family:"Tinos","Times New Roman",serif;font-weight:700;font-size:33px;color:var(--white)}
  .service{position:absolute;top:462px;color:var(--white)}
  .service-head{display:flex;align-items:center;gap:12px;height:50px}
  .service-icon{width:48px;height:48px;background:var(--white);border-radius:4px;display:flex;align-items:center;justify-content:center;flex:none}
  .service-title{font-weight:700;font-size:18px;letter-spacing:.2px}
  .service-text{margin-top:20px;font-size:14.6px;line-height:19.5px}
  .divider{position:absolute;top:462px;width:2px;height:254px;background:rgba(255,255,255,.85)}
  .footer{position:absolute;left:0;top:744px;width:1200px;height:72px;background:var(--white)}
  .footer-links{position:absolute;left:30px;top:25px;font-weight:700;font-size:17px;color:var(--ink);white-space:nowrap}
  .footer-links .sep{font-weight:400;margin:0 10px}
  .contact-band{position:absolute;left:706px;top:0;width:494px;height:72px;background:var(--blue);
    clip-path:polygon(28px 0,100% 0,100% 100%,0 100%)}
  .contact-band::before{content:"";position:absolute;left:0;top:0;width:100%;height:4px;background:var(--blue-light)}
  .contact-line{position:absolute;left:57px;top:19px;display:flex;align-items:center;gap:14px;color:var(--white);font-size:26px;white-space:nowrap}
</style>
</head>
<body>
<div class="postcard">
  <div class="hero-photo" role="img" aria-label="Photo of two business people reviewing figures on a laptop at an office desk"></div>

  <svg class="backdrop" width="1200" height="816" viewBox="0 0 1200 816" aria-hidden="true">
    <defs>
      <linearGradient id="field" x1="0" y1="0" x2="1" y2="0">
        <stop offset="0" stop-color="#1c8a33"/>
        <stop offset=".55" stop-color="#4eab3a"/>
        <stop offset="1" stop-color="#8cc63f"/>
      </linearGradient>
      <linearGradient id="sweep" x1="0" y1="1" x2="1" y2="0">
        <stop offset="0" stop-color="#5db53c"/>
        <stop offset="1" stop-color="#a6d24a"/>
      </linearGradient>
    </defs>
    <path d="M0 388 L690 388 C860 384 1040 330 1200 250 L1200 744 L0 744 Z" fill="url(#field)"/>
    <path d="M700 388 C880 380 1060 300 1200 200 L1200 290 C1060 360 900 420 700 440 Z" fill="url(#sweep)" opacity=".9"/>
    <path d="M760 744 C900 640 1060 520 1200 470 L1200 744 Z" fill="#3f9e36" opacity=".45"/>
    <path d="M690 392 C880 384 1060 310 1200 236" fill="none" stroke="#ffffff" stroke-width="3" opacity=".7"/>
  </svg>

  <div class="brand">
    <div class="brand-mark"></div>
    <div class="brand-name">MARLOW TAX PARTNERS</div>
    <div class="brand-tagline">Tax Preparation &nbsp;|&nbsp; Bookkeeping &nbsp;|&nbsp; Payroll &nbsp;|&nbsp; Entity Formation</div>
  </div>

  <h1 class="cpa-name">Eleanor Marlow, CPA<br>Professional Corporation</h1>
  <p class="promise">Individualized Business and Personal<br>Accounting services you can trust</p>

  <div class="section-tab"></div>
  <h2 class="section-title">Services</h2>

  <section class="service" style="left:30px;width:232px">
    <div class="service-head">
      <span class="service-icon"><svg width="30" height="32" viewBox="0 0 30 32"><path d="M4 2h15l7 7v21H4z" fill="none" stroke="#1667b3" stroke-width="2"/><text x="7" y="18" font-family="Arimo,sans-serif" font-size="8" font-weight="700" fill="#1667b3">TAX</text><path d="M8 23h14M8 27h10" stroke="#1667b3" stroke-width="2"/></svg></span>
      <h3 class="service-title">TAX PREPARATION</h3>
    </div>
    <p class="service-text">With over 35 years of experience filing tax returns, we are experts in tax preparation. Including Personal Returns, Corporations, LLC’s, Partnerships and State Franchise Tax Returns.</p>
  </section>
  <div class="divider" style="left:272px"></div>

  <section class="service" style="left:285px;width:290px">
    <div class="service-head">
      <span class="service-icon"><svg width="28" height="32" viewBox="0 0 28 32"><rect x="4" y="2" width="20" height="28" rx="2" fill="none" stroke="#1667b3" stroke-width="2"/><circle cx="14" cy="14" r="6" fill="none" stroke="#1667b3" stroke-width="2"/><text x="11" y="17.5" font-family="Arimo,sans-serif" font-size="9" font-weight="700" fill="#1667b3">$</text><path d="M8 25h12" stroke="#1667b3" stroke-width="2"/></svg></span>
      <h3 class="service-title">BOOKKEEPING</h3>
    </div>
    <p class="service-text">Let us take over the day-to-day bookkeeping so you can get back to running your business. We offer assistance with LedgerLine setup and provide ongoing bookkeeping services. Including frequent journal entries, accounts payables &amp; receivables, sales tax reporting &amp; payments, account reconciliation, and more.</p>
  </section>
  <div class="divider" style="left:588px"></div>

  <section class="service" style="left:606px;width:280px">
    <div class="service-head">
      <span class="service-icon"><svg width="28" height="32" viewBox="0 0 28 32"><rect x="4" y="2" width="20" height="28" rx="2" fill="none" stroke="#1667b3" stroke-width="2"/><path d="M8 12l4-4 3 3 5-5" fill="none" stroke="#1667b3" stroke-width="2"/><text x="9" y="25" font-family="Arimo,sans-serif" font-size="10" font-weight="700" fill="#1667b3">$</text><path d="M16 20h5M16 24h5" stroke="#1667b3" stroke-width="2"/></svg></span>
      <h3 class="service-title">FINANCIAL REPORTING</h3>
    </div>
    <p class="service-text">We’ll provide easy to understand financial reports that allow you and your team to manage cash flow, create budgets and make forecasting decisions. Depending on your needs, we can provide monthly, quarterly or yearly financial statements.</p>
  </section>
  <div class="divider" style="left:898px"></div>

  <section class="service" style="left:915px;width:270px">
    <div class="service-head">
      <span class="service-icon"><svg width="34" height="30" viewBox="0 0 34 30"><rect x="3" y="3" width="26" height="16" rx="2" fill="none" stroke="#1667b3" stroke-width="2"/><path d="M3 8h26" stroke="#1667b3" stroke-width="3"/><path d="M6 27l7-5h9c2 0 2-3 0-3h-6" fill="none" stroke="#1667b3" stroke-width="2"/></svg></span>
      <h3 class="service-title">PAYROLL PROCESSING</h3>
    </div>
    <p class="service-text">Whether you have 5 employees or 100+, payroll can be an overwhelming and time consuming task. We offer full-service payroll processing. Including employee onboarding, printed or direct deposit checks, quarterly payroll report filing, yearly W-2/W-3 and 1099 printing and filing, and more.</p>
  </section>

  <footer class="footer">
    <p class="footer-links">www.marlowtaxpartners.com<span class="sep">|</span>contact@marlowtaxpartners.com</p>
    <div class="contact-band">
      <div class="contact-line">
        <span>CONTACT US</span>
        <svg width="26" height="26" viewBox="0 0 26 26" aria-hidden="true"><circle cx="13" cy="13" r="11.5" fill="none" stroke="#fff" stroke-width="2"/><path d="M9 7.5l2.2 2.6-1.3 1.6c.8 1.7 2 2.9 3.7 3.7l1.6-1.3 2.6 2.2-1.4 2c-4.6-.6-8.4-4.4-9-9z" fill="#fff"/></svg>
        <span>(555) 014-2870</span>
      </div>
    </div>
  </footer>
</div>
</body>
</html>
```